Art for parenting podcast with straight/direct talk...no fluff here! "Plain Word for Families"

I need an image that will not look fluffy or soft. A no-nonsense look. This is not a 'I love parenting' podcast. It is for frustrated parents who don't know what to do. The name is 'Plain Word for Families'. The design should, therefore, NOT have hearts and flowers but, instead, look clean and direct. My logo has shades of blue so that would be nice. I have done this work for over 30 years and am well-degreed so would like the design to look stable/established. I have attached my company's logo.

Target Market(s)

Frustrated parents of children - age birth to 20

Industry/Entity Type

Coaching/Counseling for parents

Font styles to use
Serif
Sans Serif

Colors
0054AA
0677BA
7BADD7
CADEEF
E8F1F8

Requirements
Must have
• A look that is clean/bold/direct and professional. Serious.
Nice to have
• If it looks good, my name with my degrees behind my name. MS, MEd. Another thought would be to have a background image of a frustrated parent. Not sure if that would be good or look too busy.
Should not have
• Flowers, fluff, soft appearance, pinks, light colors

```html
<!DOCTYPE html>
<html lang="en">
<head>
<meta charset="utf-8">
<title>Plain Word for Families – Stationery</title>
<link rel="stylesheet" href="https://fonts.googleapis.com/css2?family=Oswald:wght@500;600&family=Montserrat:wght@500;600&display=swap">
<style>
  :root {
    --navy: #0054AA;
    --deep: #0A3F7E;
    --mid: #0677BA;
    --sky: #7BADD7;
    --mist: #CADEEF;
    --ice: #E8F1F8;
    --stage: #D3D3D3;
    --paper: #FFFFFF;
    --slate: #8A93A0;
  }
  * { box-sizing: border-box; margin: 0; padding: 0; }
  html, body { width: 1200px; height: 638px; overflow: hidden; }
  body { background: var(--stage); position: relative; font-family: "Montserrat", sans-serif; }

  /* Envelope / letterhead card */
  .envelope {
    position: absolute; left: 40px; top: 40px; width: 560px; height: 360px;
    background: var(--paper);
    border-bottom: 10px solid var(--mid);
    box-shadow: 0 6px 14px rgba(0,0,0,.25);
  }
  .envelope .brand {
    position: absolute; right: 30px; top: 34px; text-align: right;
  }
  .brand-line { display: flex; align-items: center; gap: 10px; justify-content: flex-end; }
  .brand-dot { width: 22px; height: 22px; border-radius: 50%; background: var(--mid); }
  .brand-name {
    font-family: "Oswald", sans-serif; font-weight: 500; font-size: 24px;
    color: var(--navy); letter-spacing: .5px; text-transform: uppercase;
  }
  .signatory { margin-top: 6px; font-size: 15px; font-weight: 600; color: var(--navy); letter-spacing: 1px; }
  .credentials { font-size: 12px; color: var(--slate); letter-spacing: 1px; }

  /* Postcard */
  .postcard {
    position: absolute; left: 500px; top: 150px; width: 660px; height: 450px;
    background: var(--paper); overflow: hidden;
    box-shadow: 0 8px 18px rgba(0,0,0,.3);
  }
  .postcard .photo {
    position: absolute; inset: 0;
    background: linear-gradient(135deg, #F3F1EE 0%, #E6DDD4 40%, #F1ECE4 65%, #F7F6F2 100%);
  }
  .postcard .header { position: absolute; left: 0; top: 0; width: 660px; height: 120px; }
  .postcard .title {
    position: absolute; right: 22px; top: 12px;
    font-family: "Oswald", sans-serif; font-weight: 600; font-size: 24px; color: var(--paper);
  }
  .tagline {
    position: absolute; right: 24px; top: 104px; text-align: right;
    font-family: "Oswald", sans-serif; font-weight: 500; font-size: 19px; line-height: 1.35;
    color: var(--mid);
  }
  .tagline strong { color: var(--navy); font-weight: 600; }
  .postcard .brand { position: absolute; left: 28px; bottom: 30px; }
  .postcard .footer-band {
    position: absolute; left: 0; bottom: 0; width: 100%; height: 10px; background: var(--navy);
  }
</style>
</head>
<body>
  <section class="envelope">
    <div class="brand">
      <div class="brand-line">
        <span class="brand-dot"></span>
        <span class="brand-name">Steady-On Family Guidance</span>
      </div>
      <p class="signatory">DANA MERRICK</p>
      <p class="credentials">MS, MEd.</p>
    </div>
  </section>

  <section class="postcard">
    <div class="photo" role="img" aria-label="Photo of a frustrated parent raising her voice while a daughter covers her ears on a sofa, in faded light tones"></div>
    <svg class="header" viewBox="0 0 660 120" preserveAspectRatio="none" aria-hidden="true">
      <defs>
        <linearGradient id="bandFill" x1="0" y1="0" x2="1" y2="0">
          <stop offset="0" stop-color="#0A3F7E"/>
          <stop offset="1" stop-color="#0054AA"/>
        </linearGradient>
      </defs>
      <path d="M0 0 H660 V62 C470 46 200 60 0 104 Z" fill="#C8CDD3"/>
      <path d="M0 0 H660 V50 C470 34 200 48 0 90 Z" fill="url(#bandFill)"/>
    </svg>
    <h1 class="title">Plain Word for Families</h1>
    <p class="tagline">
      Spending <strong>TIME</strong> with your children<br>
      is more important<br>
      than spending <strong>MONEY</strong> on children
    </p>
    <div class="brand">
      <div class="brand-line">
        <span class="brand-dot"></span>
        <span class="brand-name">Steady-On Family Guidance</span>
      </div>
    </div>
    <div class="footer-band"></div>
  </section>
</body>
</html>
```